Zielgruppe
Ich bin Fotograf und habe mich auf Schwangerschafts- und Neugeborenenfotografie spezialisiert. Meine Zielgruppe sind schwangere Frauen im letzten Drittel der Schwangerschaft und frisch gewordene Eltern.
Aufgabenstellung
- sehr schlichtes Design, in der Anlage finden Sie zwei der meist verkauften Karten damit Sie sich vom Stil eine Vorstellung machen können
- Lieferung als offene Indesign 5.5 Datei (so das die Farben, Texte, .... angepasst werden können)
- 2-3 Bilder (querformat) sollen in das Design eingearbeitet werden können
- Die Karten werden von mir nachher als fertig gedruckte Karte an meine Kunden verkauft, dies bitte ich zu berücksichtigen
- ich möchte die Karten so nutzen können das sowohl Geburtskarten für Jungs wie auch für Mädels erstellt werden können
- Format: Din A6 (geschlossen 105x148mm), Klappkarte, hoch, 3mm Beschnitt

```html
<!DOCTYPE html>
<html lang="de">
<head>
<meta charset="utf-8">
<title>Geburtskarte Mika – Klappkarte A6</title>
<link href="https://fonts.googleapis.com/css2?family=Amatic+SC:wght@400;700&family=Special+Elite&family=Jost:wght@300;400&display=swap" rel="stylesheet">
<style>
  :root{
    --mint:#a2c1ba;
    --slate:#6e6e6e;
    --paper:#ffffff;
    --stage-top:#f7f7f7;
    --stage-bottom:#ebebeb;
    --label:#8a8a8a;
    --ink:#555555;
    --photo-dark:#3a3a3a;
    --photo-mid:#9a9a9a;
    --photo-light:#d9d9d9;
  }
  *{margin:0;padding:0;box-sizing:border-box}
  html,body{width:1200px;height:829px;overflow:hidden}
  body{
    background:linear-gradient(180deg,var(--stage-top),var(--stage-bottom));
    position:relative;
    font-family:"Jost",sans-serif;
  }
  .spread{position:absolute;top:262px;width:486px;height:342px;display:flex}
  .spread--outside{left:71px}
  .spread--inside{left:643px}
  .panel{position:relative;width:243px;height:342px;overflow:hidden}
  .panel-label{
    position:absolute;top:-46px;width:243px;text-align:center;
    font-family:"Jost",sans-serif;font-weight:300;font-size:18px;color:var(--label);letter-spacing:.5px;
  }
  .panel-label--left{left:0}
  .panel-label--right{left:243px}

  .hand-caps{
    font-family:"Amatic SC",sans-serif;font-weight:400;text-transform:uppercase;
    color:var(--paper);line-height:1;white-space:nowrap;
  }
  .photo{background:linear-gradient(135deg,var(--photo-dark),var(--photo-mid) 55%,var(--photo-dark))}

  /* Rückseite */
  .back{background:var(--slate)}
  .credit{
    position:absolute;bottom:10px;left:0;right:0;text-align:center;
    font-family:"Jost",sans-serif;font-size:6px;color:#e4e4e4;
  }

  /* Vorderseite */
  .front{background:var(--slate);display:flex;flex-direction:column}
  .name-band{
    height:71px;background:var(--mint);border-bottom:2px solid var(--paper);
    display:flex;align-items:center;justify-content:center;
  }
  .name-band .hand-caps{font-size:50px;letter-spacing:2px}
  .front .photo{height:187px;border-bottom:2px solid var(--paper)}
  .birth-facts{flex:1;padding:9px 22px 0 23px}
  .facts-row{display:flex;align-items:center;justify-content:space-between;height:24px}
  .facts-row .hand-caps{font-size:25px;letter-spacing:.5px}
  .ruler{margin:5px 0 6px;display:block}

  /* Innenseite */
  .inside-left,.inside-right{display:flex;flex-direction:column}
  .inside-left .photo{height:189px;border-bottom:2px solid var(--paper);
    background:radial-gradient(ellipse at 40% 50%,var(--photo-mid),var(--photo-light) 70%)}
  .announce{flex:1;background:var(--mint);display:flex;align-items:center;justify-content:center;text-align:center}
  .announce .hand-caps{font-size:48px;letter-spacing:2px;line-height:.95}
  .message{height:189px;background:var(--paper);text-align:center;padding-top:24px;border-bottom:2px solid var(--paper)}
  .quote{
    font-family:"Amatic SC",sans-serif;text-transform:uppercase;color:var(--mint);
    font-size:20px;line-height:20px;letter-spacing:.6px;
  }
  .thanks{margin-top:24px;font-family:"Special Elite",serif;color:var(--ink);font-size:9.5px;line-height:15px}
  .inside-right .photo{flex:1;background:radial-gradient(ellipse at 65% 45%,var(--photo-mid),var(--photo-light) 65%)}
</style>
</head>
<body>

<section class="spread spread--outside">
  <p class="panel-label panel-label--left">Rückseite</p>
  <p class="panel-label panel-label--right">Vorderseite</p>

  <div class="panel back">
    <p class="credit">Lindqvist Fotografie</p>
  </div>

  <div class="panel front">
    <div class="name-band"><span class="hand-caps">Mika</span></div>
    <div class="photo" role="img" aria-label="Schwarzweißfoto: Neugeborenes liegt in den Händen der Eltern"></div>
    <div class="birth-facts">
      <div class="facts-row">
        <span class="hand-caps">13. März 2019</span>
        <svg width="22" height="22" viewBox="0 0 22 22" aria-hidden="true">
          <circle cx="11" cy="11" r="10" fill="#fff" stroke="var(--mint)" stroke-width="1.5"/>
          <path d="M11 5v6l-3 3" stroke="#444" stroke-width="1.6" fill="none" stroke-linecap="round"/>
        </svg>
        <span class="hand-caps">08.41 Uhr</span>
      </div>
      <svg class="ruler" width="198" height="10" viewBox="0 0 198 10" aria-hidden="true">
        <rect width="198" height="10" fill="var(--mint)"/>
        <g stroke="#fff" stroke-width="1">
          <path d="M6 0v4M18 0v3M30 0v4M42 0v3M54 0v4M66 0v3M78 0v4M90 0v3M102 0v4M114 0v3M126 0v4M138 0v3M150 0v4M162 0v3M174 0v4M186 0v3"/>
        </g>
      </svg>
      <div class="facts-row">
        <span class="hand-caps">3420 Gramm</span>
        <svg width="24" height="26" viewBox="0 0 24 26" aria-hidden="true">
          <path d="M0 0h24l-8 10h-8z" fill="var(--mint)"/>
          <path d="M8 12h8l8 14H0z" fill="var(--mint)"/>
          <circle cx="12" cy="19" r="4" fill="#fff"/>
          <path d="M12 16.5v2.5" stroke="#444" stroke-width="1"/>
        </svg>
        <span class="hand-caps">51 cm</span>
      </div>
    </div>
  </div>
</section>

<section class="spread spread--inside">
  <p class="panel-label panel-label--left">Innenseite links</p>
  <p class="panel-label panel-label--right">Innenseite rechts</p>

  <div class="panel inside-left">
    <div class="photo" role="img" aria-label="Schwarzweißfoto: Porträt des Neugeborenen, in eine Decke gehüllt"></div>
    <div class="announce"><span class="hand-caps">Mika<br>ist da!</span></div>
  </div>

  <div class="panel inside-right">
    <div class="message">
      <p class="quote">Manches beginnt klein,<br>manches beginnt groß,<br>aber manchmal ist das<br>kleinste das größte</p>
      <p class="thanks">Danke für all die<br>Glückwünsche und Geschenke!<br>Nora &amp; Felix</p>
    </div>
    <div class="photo" role="img" aria-label="Schwarzweißfoto: schlafendes Neugeborenes auf einer weichen Decke"></div>
  </div>
</section>

</body>
</html>
```